Stationery & business cards for nonprofit
WELL Wells of kindness beyond measure
Stationery & business cards for nonprofit - Religion and Spirituality
Creative Brief
Use same font as used in my logo
Ruth Pelling
President
481 Orchard Lane Birmingham, AL 35187
ruth@wellkb.org
www.wellkb.org
We are open to ideas and suggestions using our logo, this is a nonprofit that supports an orphanage and assists widows in Africa, as shown in the earth tone in the logo. Logo information: Font: Desire (manipulated), Swiss Condensed, Times Roman Color: Pantone 1395, Pantone 7407, Pantone 364 Our website is currently under development, but you can see pictures, etc to get a feel for our nonprofit by going to www.wellkb.org
We are thinking to put just the logo on the back of the card with the name (wells of kindness beyond measure) and the verse listed - I John 3:16-18
mirabelcostow mirabelcostow
AI and EPS file formats have been uploaded for use as needed.

```html
<!DOCTYPE html>
<html lang="en">
<head>
<meta charset="utf-8">
<title>WELL – Business Card</title>
<link rel="stylesheet" href="https://fonts.googleapis.com/css2?family=Open+Sans:wght@400;600;700&display=swap">
<style>
  :root{
    --backdrop:#ece9e4;
    --paper:#ffffff;
    --ink-dark:#1c1a18;
    --gold-light:#c9a44a;
    --gold:#b08a2e;
    --gold-deep:#8e6c1f;
    --green:#3f7d1e;
    --text-light:#ffffff;
    --logo-gold:#b8922f;
  }
  html,body{margin:0;padding:0;overflow:hidden}
  body{
    width:1200px;height:909px;background:var(--backdrop);
    font-family:"Open Sans",Arial,sans-serif;
    display:flex;align-items:center;justify-content:center;gap:80px;
  }
  .card{
    position:relative;width:380px;height:665px;overflow:hidden;
    box-shadow:0 10px 30px rgba(0,0,0,.18);
  }
  .card__art{position:absolute;inset:0}
  .logo{
    position:absolute;left:0;right:0;text-align:center;
  }
  .logo__name{
    display:inline-flex;align-items:center;gap:10px;
    font-weight:700;font-size:56px;letter-spacing:2px;color:var(--logo-gold);line-height:1;
  }
  .logo__dot{width:18px;height:18px;border-radius:50%;background:var(--green)}
  .logo__tagline{
    margin-top:8px;font-size:10px;font-weight:600;color:var(--green);letter-spacing:.3px;
  }
  .card--front .logo{top:70px}
  .card--back .logo{top:62px}
  .card--back .logo__tagline{color:var(--gold-light)}
  .contact{
    position:absolute;left:150px;top:340px;color:var(--text-light);
    font-size:13px;line-height:1.45;
  }
  .contact__name{font-size:18px;font-weight:700;margin:0}
  .contact__role{font-size:14px;margin:0 0 14px}
  .contact__address{margin:0 0 14px}
  .contact__line{margin:0}
  .contact__line--email{margin-top:10px}
  .contact__label{font-weight:700}
  .web{
    position:absolute;right:24px;bottom:22px;color:var(--text-light);font-size:12px;
  }
</style>
</head>
<body>

<section class="card card--front" aria-label="Business card front">
  <svg class="card__art" viewBox="0 0 380 665" preserveAspectRatio="none" aria-hidden="true">
    <defs>
      <linearGradient id="goldFront" x1="0" y1="0" x2="1" y2="1">
        <stop offset="0" stop-color="var(--gold-light)"/>
        <stop offset=".55" stop-color="var(--gold)"/>
        <stop offset="1" stop-color="var(--gold-deep)"/>
      </linearGradient>
    </defs>
    <rect width="380" height="665" fill="var(--paper)"/>
    <path d="M0 250 Q170 250 380 330 L380 665 L0 665 Z" fill="var(--green)"/>
    <path d="M0 266 Q170 264 380 346 L380 665 L0 665 Z" fill="url(#goldFront)"/>
  </svg>
  <div class="logo">
    <div class="logo__name"><span class="logo__dot"></span>WELL</div>
    <div class="logo__tagline">Wells of kindness beyond measure</div>
  </div>
  <div class="contact">
    <p class="contact__name">Talia Brook-Hanley</p>
    <p class="contact__role">Consultant</p>
    <p class="contact__address">027 12th Avenue,<br>Hill Crest Lane<br>Upper Vale 2KT</p>
    <p class="contact__line"><span class="contact__label">Ph:</span> 012 555 0147</p>
    <p class="contact__line"><span class="contact__label">Cell:</span> 012 555 0147</p>
    <p class="contact__line"><span class="contact__label">Fax:</span> 012 555 0147</p>
    <p class="contact__line contact__line--email"><span class="contact__label">Email:</span> tb@samplesite.org</p>
    <p class="contact__line">www.samplesite.org</p>
  </div>
</section>

<section class="card card--back" aria-label="Business card back">
  <svg class="card__art" viewBox="0 0 380 665" preserveAspectRatio="none" aria-hidden="true">
    <defs>
      <linearGradient id="goldBack" x1="0" y1="0" x2="1" y2="1">
        <stop offset="0" stop-color="var(--gold-light)"/>
        <stop offset=".55" stop-color="var(--gold)"/>
        <stop offset="1" stop-color="var(--gold-deep)"/>
      </linearGradient>
    </defs>
    <rect width="380" height="665" fill="var(--ink-dark)"/>
    <path d="M0 250 Q200 240 380 160 L380 665 L0 665 Z" fill="var(--green)"/>
    <path d="M0 266 Q200 256 380 178 L380 665 L0 665 Z" fill="url(#goldBack)"/>
  </svg>
  <div class="logo">
    <div class="logo__name"><span class="logo__dot"></span>WELL</div>
    <div class="logo__tagline">Wells of kindness beyond measure</div>
  </div>
  <div class="web">www.yoursamplesite.org</div>
</section>

</body>
</html>
```